Management consultant needs business cards

We need a design for a personal/professional business card for a management consultant. Work is typically focused on the b2b space, helping companies improve their operations. The final design should communicate efficiency and helping companies and people achieve their full potential.

Company name is "Copperfen Consultants"

Brand promise is "Finding Potential - Unleashing Performance"

We come from major consulting firms (Haldorne, Vesk, TQP) but would like to project a slightly more modern feel than those players.

Target Market(s)

Targeting B2B markets such as banks or companies.

Industry/Entity Type

Business

Requirements
Must have
• The card must communicate the following information:

Nolan J Brackett
Managing Director
Copperfen Consultants
Phone: 416-555-0172
nolan.brackett@copperfenconsultants.example
www.copperfenconsultants.example

214 Pellworth Ave
Toronto, ON M5X 9Z7

Back side should have
"Finding Potential - Unleashing Performance"

```html
<!DOCTYPE html>
<html lang="en">
<head>
<meta charset="utf-8">
<title>Copperfen Consultants – Business Card</title>
<link href="https://fonts.googleapis.com/css2?family=Roboto:wght@300;400;500&display=swap" rel="stylesheet">
<style>
  :root {
    --ink: #2b2b2b;
    --text: #333333;
    --paper: #ffffff;
  }
  html, body {
    margin: 0;
    padding: 0;
    width: 1200px;
    height: 686px;
    overflow: hidden;
    background: var(--paper);
  }
  .card {
    position: relative;
    width: 1200px;
    height: 686px;
    background: var(--paper);
    color: var(--text);
    font-family: "Roboto", Arial, sans-serif;
    overflow: hidden;
  }
  .abs { position: absolute; margin: 0; line-height: 1; white-space: nowrap; }
  .company-name {
    left: 80px;
    top: 280px;
    font-size: 54px;
    font-weight: 400;
    color: var(--ink);
  }
  .person-name { left: 686px; top: 79px; font-size: 58px; font-weight: 500; color: var(--ink); }
  .person-title { left: 688px; top: 141px; font-size: 36px; font-weight: 300; color: var(--text); }
  .tagline-first { left: 80px; top: 466px; font-size: 32px; font-weight: 300; }
  .tagline-second { left: 142px; top: 506px; font-size: 41px; font-weight: 300; }
  .contact-icon { position: absolute; width: 34px; height: 34px; fill: var(--ink); }
  .contact-phone { left: 750px; top: 378px; font-size: 39px; font-weight: 400; }
  .contact-email { left: 750px; top: 457px; font-size: 20px; }
  .contact-web { left: 750px; top: 521px; font-size: 20px; }
  .contact-address { left: 750px; top: 565px; font-size: 20px; line-height: 32px; white-space: normal; }
</style>
</head>
<body>
<main class="card">
  <p class="abs company-name">Copperfen Consultants</p>

  <h1 class="abs person-name">Nolan J Brackett</h1>
  <p class="abs person-title">Managing Director</p>

  <p class="abs tagline-first">Finding Potential</p>
  <p class="abs tagline-second">Unleashing Performance</p>

  <svg class="contact-icon" style="left:686px;top:383px" viewBox="0 0 24 24" aria-hidden="true">
    <path d="M6.6 10.8a15.1 15.1 0 0 0 6.6 6.6l2.2-2.2c.3-.3.7-.4 1-.2 1.1.4 2.3.6 3.6.6.6 0 1 .4 1 1V20c0 .6-.4 1-1 1A17 17 0 0 1 3 4c0-.6.4-1 1-1h3.5c.6 0 1 .4 1 1 0 1.3.2 2.5.6 3.6.1.3 0 .7-.2 1z"/>
  </svg>
  <svg class="contact-icon" style="left:686px;top:449px" viewBox="0 0 24 24" aria-hidden="true">
    <path d="M2 5h20v14H2zm2 2v.5l8 5 8-5V7zm0 2.9V17h16V9.9l-8 5z"/>
  </svg>
  <svg class="contact-icon" style="left:686px;top:513px" viewBox="0 0 24 24" aria-hidden="true">
    <path d="M12 2a10 10 0 1 0 0 20 10 10 0 0 0 0-20zm-1 17.9A8 8 0 0 1 4.2 10L9 14.8v1a2 2 0 0 0 2 2zm6.9-2.5A2 2 0 0 0 16 16h-1v-3a1 1 0 0 0-1-1H8v-2h2a1 1 0 0 0 1-1V7h2a2 2 0 0 0 2-2v-.4a8 8 0 0 1 2.9 12.8z"/>
  </svg>
  <svg class="contact-icon" style="left:686px;top:581px;width:36px;height:40px" viewBox="0 0 24 24" aria-hidden="true">
    <path d="M12 2a7 7 0 0 0-7 7c0 5.2 7 13 7 13s7-7.8 7-13a7 7 0 0 0-7-7zm0 2a5 5 0 0 1 5 5c0 3.2-3.6 8-5 9.8C10.6 17 7 12.2 7 9a5 5 0 0 1 5-5zm0 2.5a2.5 2.5 0 1 0 0 5 2.5 2.5 0 0 0 0-5z"/>
  </svg>

  <p class="abs contact-phone">416-555-0172</p>
  <p class="abs contact-email">nolan.brackett@copperfenconsultants.example</p>
  <p class="abs contact-web">www.copperfenconsultants.example</p>
  <p class="abs contact-address">214 Pellworth Ave<br>Toronto, ON M5X 9Z7</p>
</main>
</body>
</html>
```